Financial Advisor Resource Firm needs business card design

Need business card design for company in Omaha NE called Tallowbrook Alliance. We provide resources to financial advisors....workshop programs, retirement analysis, and insurance planning. I would like to see designs that use grays, greens, black, and white colors. The final design should communicate 'collaboration' and be simple yet attractive to financial planning clients. I will attached our logo and another picture of a puzzle piece coming together. I would like the incorporate the puzzle picture somehow, maybe on the back somehow, with color or just the gray scale....OR, the picture be the front of the card with 'Tallowbrook' definition on it (see upload) and then company logo, employee name, title, address on the back (see ppt uploaded). The following disclosure needs to be included somewhere- Advisory services offered through Hemstead Ledger, LLC.
Updates

I uploaded a svg and ai file of the logo

Target Market(s)

Financial planning clients and financial advisors....so pretty diverse age range of about 40-70.

Industry/Entity Type

Financial Planning

Contact Information for Business Card

Morris P. Quillfen, MBA
Founder/President
5327 E. Larkspur Avenue
Suite 418
Omaha, NE 68907
Phone- (402) 555-0147
Cell- (402) 555-0193
Fax- (402) 555-0126
email- morris@tallowbrookplan.example
web address- www.tallowbrookplan.example

Colors
1b1b1b
474747
d3d3d3
ffffff
9bcb3c
abd036

Requirements
Must have
• Must include logo provided, must be 2 sided, and must have disclosure...all of these items listed in project description

```html
<!DOCTYPE html>
<html lang="en">
<head>
<meta charset="utf-8">
<title>Tallowbrook Alliance – Business Card</title>
<link href="https://fonts.googleapis.com/css2?family=Asap:wght@400;500;600&display=swap" rel="stylesheet">
<style>
  :root {
    --canvas: #f1f1f1;
    --card: #1b1b1b;
    --card-back: #1c1c1c;
    --white: #ffffff;
    --muted: #9a9a9a;
    --green: #8cc63f;
    --green-bright: #9bcb3c;
    --photo-light: #d3d3d3;
    --photo-dark: #474747;
  }
  * { margin: 0; padding: 0; box-sizing: border-box; }
  html, body {
    width: 1200px; height: 900px; overflow: hidden;
    background: var(--canvas);
    font-family: "Asap", "Helvetica Neue", Arial, sans-serif;
  }
  .canvas { position: relative; width: 1200px; height: 900px; }
  .card {
    position: absolute;
    background: var(--card);
    box-shadow: 0 18px 30px rgba(0,0,0,0.28);
    overflow: hidden;
  }
  .card--front { left: 301px; top: 92px; width: 599px; height: 342px; }
  .card--back { left: 299px; top: 476px; width: 603px; height: 344px; background: var(--card-back); }

  .brand { position: absolute; color: var(--white); font-weight: 500; text-align: right; line-height: 1; }
  .brand__main { display: block; font-size: 27px; letter-spacing: 0.5px; }
  .brand__sub { display: block; font-size: 13px; letter-spacing: 1.5px; margin-top: 4px; }
  .card--front .brand { left: 35px; top: 136px; width: 230px; }
  .card--back .brand { left: 36px; top: 62px; width: 206px; }
  .card--back .brand__main { font-size: 24px; }
  .card--back .brand__sub { font-size: 12px; }

  .tagline {
    position: absolute; left: 0; top: 188px; width: 300px;
    text-align: center; color: var(--white); font-size: 15px; line-height: 19px;
  }
  .photo { position: absolute; left: 300px; top: 50px; }

  .person { position: absolute; right: 37px; top: 48px; text-align: right; }
  .person__name { color: var(--green); font-size: 22px; font-weight: 600; line-height: 22px; }
  .person__cred { color: var(--white); font-size: 15px; font-weight: 400; }
  .person__title { color: var(--white); font-size: 16px; line-height: 20px; }
  .person__address { color: var(--green); font-size: 16px; line-height: 19px; margin-top: 7px; }
  .accent-tab { position: absolute; right: 0; top: 56px; width: 10px; height: 28px; background: var(--green); }

  .contacts { position: absolute; left: 36px; top: 199px; list-style: none; }
  .contacts li {
    display: flex; align-items: center; height: 26px;
    color: var(--white); font-size: 15.5px;
  }
  .contacts svg { width: 17px; height: 17px; margin-right: 12px; fill: var(--green); flex: none; }
  .website { position: absolute; right: 37px; top: 280px; color: var(--white); font-size: 15.5px; }
  .website span { color: var(--green); }
  .disclosure {
    position: absolute; left: 0; right: 0; bottom: 10px;
    text-align: center; color: var(--muted); font-size: 9px; letter-spacing: 0.2px;
  }
</style>
</head>
<body>
<main class="canvas">

  <section class="card card--front" aria-label="Card front">
    <div class="brand">
      <span class="brand__main">TALLOWBROOK</span>
      <span class="brand__sub">ALLIANCE</span>
    </div>
    <p class="tagline">To come together and unite<br>in common interest and focus</p>
    <svg class="photo" width="270" height="240" viewBox="0 0 270 240">
      <defs>
        <linearGradient id="photoTone" x1="0" y1="0" x2="1" y2="1">
          <stop offset="0" stop-color="#e4e4e4"/>
          <stop offset="0.55" stop-color="#9a9a9a"/>
          <stop offset="1" stop-color="#3f3f3f"/>
        </linearGradient>
      </defs>
      <path d="M60 28 C95 10 160 20 200 40 C230 55 200 120 190 170 C178 225 130 240 80 225 C30 210 -5 150 5 100 C12 65 35 40 60 28 Z" fill="var(--green)"/>
      <path role="img" aria-label="Black and white photo of several hands fitting puzzle pieces together"
        d="M70 18 C110 -2 200 0 245 35 C275 60 262 110 235 150 C205 195 170 230 115 235 C60 240 15 200 10 140 C5 85 35 38 70 18 Z"
        fill="url(#photoTone)"/>
    </svg>
  </section>

  <section class="card card--back" aria-label="Card back">
    <div class="brand">
      <span class="brand__main">TALLOWBROOK</span>
      <span class="brand__sub">ALLIANCE</span>
    </div>

    <div class="person">
      <p class="person__name">Morris P. Quillfen<span class="person__cred">, MBA</span></p>
      <p class="person__title">Founder | President</p>
      <p class="person__address">5327 E. Larkspur Avenue<br>Suite 418, Omaha, NE 68907</p>
    </div>
    <span class="accent-tab"></span>

    <ul class="contacts">
      <li>
        <svg viewBox="0 0 24 24" aria-hidden="true"><path d="M6.6 10.8c1.4 2.8 3.8 5.1 6.6 6.6l2.2-2.2c.3-.3.7-.4 1-.2 1.1.4 2.3.6 3.6.6.6 0 1 .4 1 1V20c0 .6-.4 1-1 1C10.6 21 3 13.4 3 4c0-.6.4-1 1-1h3.5c.6 0 1 .4 1 1 0 1.3.2 2.5.6 3.6.1.3 0 .7-.2 1l-2.3 2.2z"/></svg>
        (402) 555 - 0147
      </li>
      <li>
        <svg viewBox="0 0 24 24" aria-hidden="true"><path d="M7 1h10a2 2 0 0 1 2 2v18a2 2 0 0 1-2 2H7a2 2 0 0 1-2-2V3a2 2 0 0 1 2-2zm0 3v14h10V4H7zm5 15.2a1.2 1.2 0 1 0 0 2.4 1.2 1.2 0 0 0 0-2.4z"/></svg>
        (402) 555 - 0193
      </li>
      <li>
        <svg viewBox="0 0 24 24" aria-hidden="true"><path d="M2 5h4v16H2zM8 3h10l4 4v14H8zm3 9v2h2v-2zm4 0v2h2v-2zm-4 4v2h2v-2zm4 0v2h2v-2zM11 6v3h8V7.5L17.5 6z"/></svg>
        (402) 555 - 0126
      </li>
      <li>
        <svg viewBox="0 0 24 24" aria-hidden="true"><path d="M2 5h20v2l-10 6L2 7zm0 4.3l10 6 10-6V19H2z"/></svg>
        morris@tallowbrookplan.example
      </li>
    </ul>

    <p class="website">www.<span>tallowbrookplan</span>.example</p>
    <p class="disclosure">Advisory services offered through Hemstead Ledger, LLC</p>
  </section>

</main>
</body>
</html>
```